Website Redesign using existing images, copy etc.

I'm looking for a website redesign/refresh of my current WordPress website. I would like to utilize the same photography, a new photo viewer, and an overall refresh of the entire design. This will need to be WordPress with simple accessibility to make changes as we add additional properties and make updates. We auction luxury real estate and luxury yachts for non-distressed sellers. It needs to be simple, luxurious and with ease of use for both web and especially mobile. www.MarlowenGroup.com

```html
<!DOCTYPE html>
<html lang="en">
<head>
<meta charset="utf-8">
<title>Marlowen Group — Real Estate &amp; Yachts</title>
<link href="https://fonts.googleapis.com/css2?family=Poppins:wght@300;400;500;600;700&display=swap" rel="stylesheet">
<style>
:root{
  --gold:#9a8159;
  --gold-dark:#7f6a47;
  --ink:#1f1f1f;
  --text:#444;
  --muted:#777;
  --light:#efefef;
  --mid:#dcdcdc;
  --white:#fff;
  --footer:#2a2a2a;
}
*{box-sizing:border-box;margin:0;padding:0}
html,body{width:1200px;height:4660px;overflow:hidden}
body{font-family:'Poppins',sans-serif;color:var(--text);background:var(--white);position:relative}
.abs{position:absolute}
.eyebrow{font-size:15px;font-weight:600;letter-spacing:1px;color:var(--gold);text-transform:uppercase}
.rule{width:70px;height:3px;background:var(--gold);margin:8px 0 10px}
.center{text-align:center}
.center .rule{margin-left:auto;margin-right:auto}
.h2{font-size:34px;font-weight:600;color:var(--ink);line-height:1.2}
.body-copy{font-size:15px;line-height:1.75;color:var(--text)}
.btn{display:inline-flex;align-items:center;gap:10px;background:var(--gold);color:var(--white);font-size:14px;font-weight:500;letter-spacing:1px;padding:12px 22px;text-transform:uppercase}
.btn svg{width:10px;height:10px}
/* header */
.site-header{left:0;top:0;width:1200px;height:128px;background:var(--white)}
.phone{left:16px;top:8px;font-size:15px;font-weight:500;color:var(--ink);display:flex;align-items:center;gap:8px}
.brand{left:44px;top:52px;display:flex;align-items:center;gap:12px;font-size:20px;font-weight:600;color:var(--ink)}
.brand .dot{width:40px;height:40px;border-radius:50%;border:3px solid var(--ink)}
.nav{right:40px;top:82px;font-size:15px;font-weight:500;color:var(--ink);display:flex;gap:14px}
/* hero */
.hero{left:0;top:128px;width:1200px;height:700px;background:linear-gradient(180deg,#c9cdcf 0%,#a9aeb1 45%,#8b8f91 100%)}
.play{left:560px;top:200px;width:80px;height:80px;border-radius:50%;background:rgba(255,255,255,.92)}
.hero-title{left:0;top:455px;width:1200px;font-size:62px;font-weight:600;color:var(--white)}
.hero-sub{left:0;top:565px;width:1200px;font-size:22px;color:var(--white)}
.hero-btns{left:0;top:640px;width:1200px;display:flex;justify-content:center;gap:28px}
.hero-btns .btn{font-size:13px;padding:10px 18px}
/* about */
.about{left:0;top:828px;width:1200px;height:560px;background:var(--white)}
.about-text{left:40px;top:72px;width:540px}
.about-frame{left:660px;top:60px;width:340px;height:452px;background:var(--light);border:14px solid var(--white);outline:2px solid var(--mid)}
/* billion */
.billion{left:0;top:1388px;width:1200px;height:500px;background:linear-gradient(160deg,var(--light) 55%,#e2e2e2 55%)}
.circle-photo{left:70px;top:12px;width:440px;height:440px;border-radius:50%;background:linear-gradient(180deg,#cfd8df,#e8eaeb 55%,#7aa3b8);border:10px solid var(--white)}
.billion-text{left:610px;top:120px;width:530px}
/* success */
.success{left:0;top:1960px;width:1200px;height:840px}
.card{top:190px;height:280px}
.card-dark{left:48px;width:532px;background:linear-gradient(180deg,#1d2430,#39414d 70%,#232323)}
.card-light{left:620px;width:532px;background:linear-gradient(180deg,#b9d3ec,#c8b796 60%,#6f8a4a)}
.card-label{font-size:22px;font-weight:500;color:var(--white)}
.arrow{top:518px;width:40px;height:40px;border-radius:50%;background:var(--white);border:2px solid var(--gold);display:flex;align-items:center;justify-content:center}
/* press */
.press{left:0;top:2820px;width:1200px;height:550px;background:linear-gradient(180deg,#f6f6f6,#ececec)}
.pill{top:172px;width:200px;height:108px;border-radius:54px;background:var(--white);box-shadow:0 2px 8px rgba(0,0,0,.08);display:flex;align-items:center;justify-content:center}
.pill span{width:120px;height:26px;background:#d0d0d0;border-radius:4px}
/* upcoming */
.upcoming{left:0;top:3380px;width:1200px;height:320px;background:linear-gradient(180deg,#3d3c3a,#262523 70%,#5b5752)}
.btn-outline{border:2px solid var(--white);background:transparent}
/* newsletter */
.newsletter{left:0;top:3720px;width:1200px;height:600px;background:linear-gradient(200deg,var(--white) 55%,var(--light) 55%)}
.news-frame{left:72px;top:60px;width:480px;height:480px;background:var(--white);border:2px solid var(--mid);padding:18px}
.news-frame div{width:100%;height:100%;background:linear-gradient(180deg,#d9d5cd,#a89f8f 60%,#5d5a55)}
.field{left:636px;width:470px;height:52px;border:1px solid var(--mid);background:var(--white);font-size:14px;color:var(--muted);padding:15px 18px}
/* footer */
.footer{left:0;top:4320px;width:1200px;height:340px;background:var(--footer);color:var(--white)}
.foot-links{left:0;top:100px;width:1200px;display:flex;justify-content:center;gap:14px;font-size:14px;font-weight:500}
.socials{left:0;top:170px;width:1200px;display:flex;justify-content:center;gap:12px}
.socials span{width:30px;height:30px;border-radius:50%;background:var(--white)}
.foot-rule{left:340px;top:225px;width:520px;height:1px;background:#555}
.legal{left:0;top:250px;width:1200px;display:flex;justify-content:center;gap:70px;font-size:13px;font-weight:500}
.seal{left:64px;top:228px;width:76px;height:76px;border-radius:50%;border:3px solid var(--gold)}
</style>
</head>
<body>

<header class="abs site-header">
  <div class="abs phone">
    <svg width="16" height="16" viewBox="0 0 24 24"><path fill="#1f1f1f" d="M6.6 10.8a15 15 0 0 0 6.6 6.6l2.2-2.2a1 1 0 0 1 1-.25 11.4 11.4 0 0 0 3.6.57 1 1 0 0 1 1 1V20a1 1 0 0 1-1 1A17 17 0 0 1 3 4a1 1 0 0 1 1-1h3.5a1 1 0 0 1 1 1c0 1.25.2 2.45.57 3.57a1 1 0 0 1-.25 1z"/></svg>
    800-555-0142
  </div>
  <div class="abs brand"><span class="dot"></span>Marlowen Group</div>
  <nav class="abs nav"><span>BUY</span><span>|</span><span>SELL</span><span>|</span><span>ABOUT</span><span>|</span><span>CONTACT</span></nav>
</header>

<section class="abs hero" role="img" aria-label="Photo of a scale house model resting on architectural blueprints">
  <div class="abs play"><svg width="80" height="80" viewBox="0 0 80 80"><path d="M33 26 L56 40 L33 54 Z" fill="#1f1f1f"/></svg></div>
  <h1 class="abs hero-title center">Marlowen Group</h1>
  <p class="abs hero-sub center">Real Estate &amp; Yachts</p>
  <div class="abs hero-btns">
    <span class="btn">Browse Upcoming Auctions <svg viewBox="0 0 10 10"><path d="M2 0 L8 5 L2 10Z" fill="#fff"/></svg></span>
    <span class="btn">Browse Past Successes <svg viewBox="0 0 10 10"><path d="M2 0 L8 5 L2 10Z" fill="#fff"/></svg></span>
  </div>
</section>

<section class="abs about">
  <svg class="abs" style="left:0;top:0" width="1200" height="560"><polygon points="0,0 620,0 380,560 0,560" fill="#efefef"/><polygon points="880,560 1200,200 1200,560" fill="#e4e4e4"/></svg>
  <div class="abs about-text">
    <div class="eyebrow">About Us</div>
    <div class="rule"></div>
    <h2 class="h2">Our Company</h2>
    <p class="body-copy" style="margin-top:14px">Have you ever experienced a sense of purpose in your life? I consider myself fortunate enough to have felt it not once, but twice. At the age of 19, I realized my first calling as a paratrooper in the US Army. Although I enjoyed being a paratrooper, I knew it couldn't last forever. After completing my service, I ventured into the advertising industry. Although it was a good experience, I always wondered if there was a second calling for me.</p>
    <p class="body-copy" style="margin-top:20px">And that's when it happened – I discovered my true passion for real</p>
    <span class="btn" style="margin-top:56px">Read More <svg viewBox="0 0 10 10"><path d="M2 0 L8 5 L2 10Z" fill="#fff"/></svg></span>
  </div>
  <div class="abs about-frame" role="img" aria-label="Photo of a modern luxury home with a pool at dusk"><div style="width:100%;height:100%;background:linear-gradient(180deg,#7fa9d6,#d8d2c4 60%,#3c4a52)"></div></div>
</section>

<section class="abs billion">
  <div class="abs circle-photo" role="img" aria-label="Photo of a white modern villa with a pool"></div>
  <div class="abs billion-text">
    <div class="eyebrow" style="font-size:14px;text-transform:none">Real Estate &amp; Yachts</div>
    <div class="rule"></div>
    <h2 class="h2" style="font-size:30px">Over One Billion Dollars of Auctions Marketed</h2>
    <p class="body-copy" style="margin-top:18px;font-size:14px">The experience of hearing the auctioneer's final proclamation of "SOLD!" is unparalleled. Whether it's the initial meeting with the seller at their estate or yacht, or the triumphant raising of the paddle by the winning buyer, we relish every moment of the process and the ensuing festivities. We're confident that you will, too.</p>
  </div>
</section>

<section class="abs success">
  <div class="abs center" style="left:0;top:48px;width:1200px">
    <div class="eyebrow" style="font-size:14px">Success Story</div>
    <div class="rule"></div>
    <h2 class="h2">Sold by Marlowen Group</h2>
  </div>
  <div class="abs card card-dark" role="img" aria-label="Photo of a sold waterfront home at night in Naples, Florida">
    <div class="abs card-label" style="left:160px;top:100px">Naples | Florida</div>
    <div class="abs" style="left:160px;top:148px;border:2px solid #fff;color:#fff;font-size:13px;padding:6px 14px">SUCCESS STORY &#9656;</div>
  </div>
  <div class="abs card card-light" role="img" aria-label="Photo of a sold Florida home with a green lawn">
    <div class="abs card-label" style="left:190px;top:226px">Naples | Florida</div>
  </div>
  <div class="abs arrow" style="left:548px"><svg width="12" height="12" viewBox="0 0 10 10"><path d="M7 0 L2 5 L7 10" stroke="#9a8159" stroke-width="2" fill="none"/></svg></div>
  <div class="abs arrow" style="left:612px"><svg width="12" height="12" viewBox="0 0 10 10"><path d="M3 0 L8 5 L3 10" stroke="#9a8159" stroke-width="2" fill="none"/></svg></div>
  <p class="abs body-copy center" style="left:48px;top:570px;width:1104px;font-size:14px">Marlowen Group is a top-tier destination for luxury property auctions, having overseen the auction marketing of numerous high-end estates and yachts. Our team of luxury home auction experts is committed to helping property owners obtain the best value for their assets while ensuring a timely sale. Whether you have an expansive compound or a metropolitan penthouse, Marlowen Group has the necessary skills and expertise to facilitate various luxury real estate auctions. Our team takes care of every aspect of the process in cooperation with your realtor, including property tours, photography and cinematography, marketing, advertising, public relations and more. Apart from high-end real estate auctions, we also organize and execute luxury yacht auctions to help boat owners find qualified buyers. Interested in finding out more about our luxury home and yacht auctions? Explore our current listings and success stories!</p>
</section>

<section class="abs press">
  <div class="abs center" style="left:0;top:24px;width:1200px">
    <div class="eyebrow" style="font-size:14px">Latest Press</div>
    <div class="rule"></div>
    <h2 class="h2">As Featured In</h2>
  </div>
  <div class="abs pill" style="left:40px"><span></span></div>
  <div class="abs pill" style="left:268px"><span></span></div>
  <div class="abs pill" style="left:496px"><span></span></div>
  <div class="abs pill" style="left:724px"><span></span></div>
  <div class="abs pill" style="left:952px"><span></span></div>
  <p class="abs body-copy center" style="left:180px;top:330px;width:840px;font-size:14px">By offering top-tier properties and vessels globally, along with strategic auction dates, exceptional marketing tactics, and a diligent public relations team, even the most prominent media outlets have taken notice. Check out some of our latest press features.</p>
  <span class="abs btn" style="left:526px;top:448px">View Press <svg viewBox="0 0 10 10"><path d="M2 0 L8 5 L2 10Z" fill="#fff"/></svg></span>
</section>

<section class="abs upcoming" role="img" aria-label="Photo of a dim luxury living room interior">
  <div class="abs center" style="left:0;top:82px;width:1200px;color:#fff">
    <div class="eyebrow" style="font-size:14px;color:#fff">Browse</div>
    <div class="rule" style="background:#fff"></div>
    <h2 class="h2" style="color:#fff">Upcoming Auctions</h2>
    <span class="btn btn-outline" style="margin-top:20px">View More <svg viewBox="0 0 10 10"><path d="M2 0 L8 5 L2 10Z" fill="#fff"/></svg></span>
  </div>
</section>

<section class="abs newsletter">
  <div class="abs news-frame" role="img" aria-label="Photo of a bright modern interior with staircase"><div></div></div>
  <div class="abs" style="left:636px;top:160px">
    <div class="eyebrow" style="font-size:14px">Newsletter</div>
    <div class="rule"></div>
    <h2 class="h2" style="font-size:30px">SIGN UP FOR MARLOWEN ALERTS</h2>
  </div>
  <div class="abs field" style="top:268px">Name</div>
  <div class="abs field" style="top:366px">Your Email</div>
  <span class="abs btn" style="left:636px;top:462px">Submit <svg viewBox="0 0 10 10"><path d="M2 0 L8 5 L2 10Z" fill="#fff"/></svg></span>
</section>

<footer class="abs footer">
  <div class="abs center" style="left:0;top:44px;width:1200px">
    <div class="eyebrow" style="font-size:13px">Quick Links</div>
    <div class="rule" style="width:50px;height:2px"></div>
  </div>
  <nav class="abs foot-links"><span>HOME</span><span>|</span><span>BUY</span><span>|</span><span>SELL</span><span>|</span><span>ABOUT</span><span>|</span><span>BLOG</span><span>|</span><span>CONTACT</span></nav>
  <div class="abs center eyebrow" style="left:0;top:142px;width:1200px;font-size:13px">Follow</div>
  <div class="abs socials"><span></span><span></span><span></span><span></span></div>
  <div class="abs foot-rule"></div>
  <div class="abs legal"><span>TERMS OF SERVICE</span><span>COPYRIGHT POLICY</span><span>PRIVACY POLICY</span></div>
  <div class="abs seal" role="img" aria-label="Veteran-owned business badge"></div>
</footer>

</body>
</html>
```